Flyer für Unternehmensberatung für betriebliche Gesundheitsförderung
Zielgruppe
Unternehmensberatung für betriebliche Gesundheitsförderung - wir machen Mitarbeiter gesünder und leistungsfähiger
Aufgabenstellung
Ich lege Textmaterial als Vorlage bei

```html
<!DOCTYPE html>
<html lang="de">
<head>
<meta charset="utf-8">
<title>Unternehmensberatung Thomas Kessler – Broschüre</title>
<link rel="stylesheet" href="https://fonts.googleapis.com/css2?family=Josefin+Sans:wght@300;400;600;700&family=Merriweather:wght@300;400;700&display=swap">
<style>
:root{
  --bg:#eeeeef;
  --cream:#fcecc8;
  --blue:#3f82b5;
  --blue-light:#9dbfdc;
  --ink:#1b1b1b;
  --text:#3a3a3a;
  --black:#0f0f0f;
  --gold:#eac98c;
  --white:#ffffff;
}
*{box-sizing:border-box;margin:0;padding:0}
html,body{width:750px;height:1200px;overflow:hidden}
body{background:var(--bg);position:relative;font-family:'Merriweather',serif}

.page{position:absolute;width:426px;height:602px;transform-origin:0 0;overflow:hidden;background:var(--white);
  font-family:'Merriweather',serif;color:var(--text);font-size:6.6px;line-height:1.62;box-shadow:0 1px 3px rgba(0,0,0,.08)}
.page p{margin-bottom:4px}
.block{position:absolute}

.brand{position:absolute;top:28px;right:28px;font-family:'Josefin Sans',sans-serif;font-weight:600;font-size:13px;color:var(--ink);letter-spacing:.3px}

.h{font-family:'Josefin Sans',sans-serif;font-weight:700;font-size:9px;line-height:1.35;color:var(--ink);padding-left:11px;position:relative;margin-bottom:5px}
.h::before{content:"";position:absolute;left:0;top:2px;width:4px;height:4px;background:var(--ink)}
.h.soft::before{background:var(--gold)}

.dots{list-style:none;margin-bottom:6px}
.dots li{position:relative;padding-left:11px}
.dots li::before{content:"";position:absolute;left:2px;top:3.6px;width:3px;height:3px;border-radius:50%;background:var(--blue)}

.ticks{list-style:none}
.ticks li{position:relative;padding-left:13px}
.ticks li::before{content:"";position:absolute;left:0;top:2.2px;width:6px;height:6px;border:.8px solid var(--blue)}
.ticks li::after{content:"";position:absolute;left:2.2px;top:2.4px;width:2px;height:4px;border-right:1px solid var(--blue);border-bottom:1px solid var(--blue);transform:rotate(40deg)}

.price{color:var(--blue);font-weight:700;font-size:8px;margin-bottom:2px}
.label{font-weight:700;color:var(--ink)}

.foot{position:absolute;left:0;bottom:0;width:100%;height:25px;background:var(--black);color:var(--gold);
  font-size:6px;display:flex;align-items:center;justify-content:flex-end;padding-right:30px;gap:18px}
.foot b{font-weight:700}
.foot span{color:#c9c2b4}

.photo{position:absolute}

.cover{background:var(--cream)}
.cover .brand{top:48px;right:0;left:0;text-align:center;font-size:25px;font-weight:600}
.cover .photo{top:105px;left:0;width:426px;height:330px;
  background:linear-gradient(180deg,var(--cream) 0%,#ead3ae 18%,#d9b994 45%,#e8d2b4 72%,var(--cream) 100%)}
.cover-title{position:absolute;top:424px;left:0;width:100%;text-align:center;font-family:'Josefin Sans',sans-serif;
  font-weight:700;font-size:26.5px;line-height:1.22;color:var(--ink);letter-spacing:.4px}
.cover-sub{position:absolute;top:499px;left:0;width:100%;text-align:center;font-family:'Josefin Sans',sans-serif;
  font-weight:400;font-size:16px;color:var(--ink);letter-spacing:.3px}
.cover-bar{position:absolute;top:530px;left:39px;width:349px;height:20px;background:var(--blue);color:var(--white);
  font-size:10px;font-weight:700;display:flex;align-items:center;padding-left:10px;gap:7px;border-radius:2px}
.cover-bar svg{width:7px;height:8px}
.cover-foot{position:absolute;bottom:0;left:0;width:100%;height:27px;background:var(--black);color:var(--white);
  font-size:10.5px;font-weight:700;display:flex;align-items:center;justify-content:center}

.box{position:absolute;background:var(--cream)}
.steps .num{color:var(--ink);font-weight:700;margin-right:8px}
.step{display:flex;margin-bottom:9px}
.step div{flex:1}
.icon-row{display:grid;grid-template-columns:1fr 1fr;gap:10px 14px;margin:6px 0 12px 6px}
.icon-item{display:flex;gap:10px;align-items:flex-start}
.icon-item svg{width:18px;height:18px;flex:none}
.inline-ticks{display:flex;gap:16px;list-style:none;margin-left:6px}
.inline-ticks li{position:relative;padding-left:11px}
.inline-ticks li::before{content:"";position:absolute;left:0;top:2.2px;width:6px;height:6px;border:.8px solid var(--blue)}
.inline-ticks li::after{content:"";position:absolute;left:2.2px;top:2.4px;width:2px;height:4px;border-right:1px solid var(--blue);border-bottom:1px solid var(--blue);transform:rotate(40deg)}
.bignum{display:flex;gap:14px;margin-bottom:6px}
.bignum .n{font-family:'Josefin Sans',sans-serif;font-size:18px;color:var(--blue-light);line-height:1;width:20px;flex:none}
.contact-line{display:flex;align-items:center;gap:7px;margin-bottom:1px}
.contact-line svg{width:7px;height:7px;flex:none}
.cta{color:var(--blue);font-family:'Josefin Sans',sans-serif;font-weight:700;font-size:8.5px;margin-bottom:6px}
.contact-band{position:absolute;left:0;bottom:25px;width:100%;height:24px;background:var(--blue);color:var(--white);
  font-size:6px;display:flex;align-items:center;justify-content:space-around;padding:0 20px}
.contact-tab{position:absolute;left:50%;transform:translateX(-50%);bottom:47px;background:var(--blue);color:var(--white);
  font-family:'Josefin Sans',sans-serif;font-weight:700;font-size:6.5px;padding:3px 18px;white-space:nowrap}
.closing{position:absolute;left:0;bottom:0;width:100%;height:25px;background:var(--black);color:var(--white);
  font-family:'Josefin Sans',sans-serif;font-weight:600;font-size:8.5px;display:flex;align-items:center;justify-content:center}
</style>
</head>
<body>

<section class="page cover" style="left:208px;top:22px;transform:scale(.78)">
  <div class="brand">Thomas Kessler</div>
  <div class="photo" role="img" aria-label="Foto: fröhliches Team mit erhobenen Armen im hellen Büro"></div>
  <h1 class="cover-title">Unternehmensberatung<br>Thomas Kessler, MBA</h1>
  <p class="cover-sub">Gesunde Mitarbeitende. Starke Unternehmen.</p>
  <div class="cover-bar"><svg viewBox="0 0 7 8"><path d="M0 0L7 4L0 8Z" fill="#fff"/></svg>Mit dem VMA Score zu messbarem Unternehmenserfolg</div>
  <div class="cover-foot">www.thomas-kessler.com</div>
</section>

<section class="page cover" style="left:36px;top:532px;transform:scale(.496)">
  <div class="brand">Thomas Kessler</div>
  <div class="photo" role="img" aria-label="Foto: fröhliches Team mit erhobenen Armen im hellen Büro"></div>
  <h1 class="cover-title">Unternehmensberatung<br>Thomas Kessler, MBA</h1>
  <p class="cover-sub">Gesunde Mitarbeitende. Starke Unternehmen.</p>
  <div class="cover-bar"><svg viewBox="0 0 7 8"><path d="M0 0L7 4L0 8Z" fill="#fff"/></svg>Mit dem VMA Score zu messbarem Unternehmenserfolg</div>
  <div class="cover-foot">www.thomas-kessler.com</div>
</section>

<section class="page" style="left:269px;top:532px;transform:scale(.496)">
  <div class="brand">Thomas Kessler</div>
  <div class="block" style="top:70px;left:38px;width:350px">
    <h2 class="h soft">Zielsetzung: Gesundheit trifft Produktivität</h2>
    <p>Unser Ziel ist die Symbiose aus gesunden, motivierten Mitarbeitenden und messbar besseren Unternehmensergebnissen. Mit unserem weltweit einzigartigen Programm reduzieren Sie nicht nur in erheblichem Ausmaß Fehlzeiten, sondern steigern nachhaltig die Leistungsfähigkeit Ihrer Teams.</p>
    <h2 class="h soft" style="margin-top:12px">Ergebnisse auf einen Blick:</h2>
    <ul class="dots">
      <li>Deutliche Reduktion von Erschöpfung und Lebensstilbedingter Müdigkeit</li>
      <li>Stark spürbarer Rückgang von Absentismus am Arbeitsplatz (wie beispielsweise durch Krankenstand)</li>
      <li>Prävention von Burnout &amp; Depressionen</li>
      <li>Langfristige Bindung von Leistungsträgern</li>
      <li>Weniger Fluktuation = geringere Kosten für Wiedereinstellung &amp; Einschulung</li>
      <li>Positionierung als attraktiver Arbeitgeber im „War for Talents“</li>
    </ul>
    <h2 class="h soft" style="margin-top:12px">Der VMA Score – Ihr Benchmark für Unternehmenserfolg</h2>
    <p>Der VitalMotivationAktivität Score (VMA Score) ist ein innovatives Messsystem, das den Zusammenhang zwischen Gesundheit, Motivation und Unternehmenserfolg sichtbar macht.</p>
  </div>
  <div class="box" style="top:365px;left:18px;width:390px;height:200px;padding:22px 20px">
    <h2 class="h">So funktioniert es:</h2>
    <div class="icon-row">
      <div class="icon-item"><svg viewBox="0 0 18 18" fill="none" stroke="#3f82b5" stroke-width="1"><rect x="4" y="2" width="10" height="14" rx="1"/><path d="M7 6h4M7 9h4M7 12h3"/></svg><span>Erhebung von Gesundheits- &amp; Leistungsdaten zum Programmstart</span></div>
      <div class="icon-item"><svg viewBox="0 0 18 18" fill="none" stroke="#3f82b5" stroke-width="1"><rect x="2" y="3" width="11" height="13" rx="1"/><path d="M5 7h5M5 10h5"/><circle cx="13" cy="12" r="3"/><path d="M15 14l2 2"/></svg><span>Auswertung anhand vorhandener Absentismus- &amp; Kostenstellenkennzahlen</span></div>
      <div class="icon-item"><svg viewBox="0 0 18 18" fill="none" stroke="#3f82b5" stroke-width="1"><rect x="3" y="2" width="12" height="14" rx="1"/><path d="M5 6l1.5 1.5L9 5M5 11l1.5 1.5L9 10M11 6h2M11 11h2"/></svg><span>Ursachenanalyse: Ernährung, Fitness, Schlafqualität, Resilienz &amp; Stressmanagement</span></div>
      <div class="icon-item"><svg viewBox="0 0 18 18" fill="none" stroke="#3f82b5" stroke-width="1"><circle cx="9" cy="9" r="6"/><circle cx="9" cy="9" r="2.5"/><path d="M9 1v2M9 15v2M1 9h2M15 9h2"/></svg><span>Ableitung konkreter Maßnahmen zur Optimierung</span></div>
    </div>
    <h2 class="h">Der VMA Score – Ihr Benchmark für Unternehmenserfolg</h2>
    <ul class="inline-ticks"><li>Messbar</li><li>Nachweisbar</li><li>Reproduzierbar</li></ul>
  </div>
  <div class="foot"><span><b style="color:var(--gold)">Unternehmensberatung</b> | Thomas Kessler, MBA</span><b>2</b></div>
</section>

<section class="page" style="left:502px;top:532px;transform:scale(.496)">
  <div class="box" style="top:0;left:0;width:426px;height:410px"></div>
  <div class="photo" style="top:0;left:0;width:215px;height:410px;background:linear-gradient(90deg,#3a3430 0%,#6b5a4b 45%,#b89f82 80%,var(--cream) 100%)" role="img" aria-label="Porträtfoto des Beraters im dunklen Pullover"></div>
  <div class="brand">Thomas Kessler</div>
  <div class="block" style="top:80px;left:190px;width:210px">
    <h2 class="h">Der Weg zum Erfolg: 3 Schritte</h2>
    <div class="steps" style="margin-top:10px;padding-left:10px">
      <div class="step"><span class="num">01</span><div>Information – Inspiration – Motivation<br>Zu Beginn steht ein emotionaler Impulsvortrag von Thomas Kessler, dessen eigene Heldengeschichte bereits tausende Menschen zu einem gesünderen, leistungsfähigeren Lebensstil inspiriert hat. Die Aufzeichnung steht auch jenen zur Verfügung, die nicht live teilnehmen können.</div></div>
      <div class="step"><span class="num">02</span><div>Analyse &amp; Erhebung<br>Parallel zur Motivationsphase erfolgt eine umfassende Datenerhebung – die Grundlage für den individuellen VMA Score und den maßgeschneiderten Maßnahmenplan.</div></div>
      <div class="step"><span class="num">03</span><div>Umsetzung &amp; Transformation<br>Begleitet durch App, Lernplattform und Expertenteam entsteht eine nachhaltige Veränderung im Arbeitsalltag – dokumentiert und sichtbar über die Entwicklung des VMA Scores.</div></div>
    </div>
  </div>
  <div class="block" style="top:352px;left:50px;color:var(--ink)"><div style="font-family:'Josefin Sans',sans-serif;font-weight:700;font-size:9.5px">Thomas Kessler, MBA</div><div>Unternehmensberater</div></div>
  <div class="block" style="top:432px;left:38px;width:360px">
    <h2 class="h">Ergebnisse auf einen Blick:</h2>
    <ul class="dots">
      <li>Wie leistungsfähig sind meine Mitarbeitenden – heute und in Zukunft?</li>
      <li>Welche finanziellen Verluste entstehen durch Fehlzeiten und reduzierte Produktivität?</li>
      <li>Wie viel Potenzial steckt in gesünderen, motivierteren Teams?</li>
      <li>Welche Kosten verursachen unnötige Austritte &amp; Re-Recruiting?</li>
      <li>Was kann ich tun, um diese Verluste in nachhaltige Gewinne zu verwandeln?</li>
      <li>Und zuletzt die wichtigste Frage: Was läuft in meinem Unternehmen nicht optimal, respektive warum ist das ermittelte Einsparungspotential so hoch? Und ja, die Zahlen werden Sie beeindrucken, lassen Sie sich von uns überraschen!</li>
    </ul>
  </div>
  <div class="foot"><span><b style="color:var(--gold)">Unternehmensberatung</b> | Thomas Kessler, MBA</span><b>3</b></div>
</section>

<section class="page" style="left:36px;top:851px;transform:scale(.496)">
  <div class="brand">Thomas Kessler</div>
  <div class="block" style="top:78px;left:38px;width:160px">
    <h2 class="h">Leistungen &amp; Investitionen</h2>
    <div style="padding-left:11px">
      <p class="label" style="margin-bottom:2px">Impulsvortrag von Thomas Kessler:</p>
      <p class="price">€ 25.000</p>
      <p>(inkl. Aufzeichnung)</p>
      <p class="label" style="margin:6px 0 2px">Laufende Programmkosten:</p>
      <p class="price">€ 5,90 / Mitarbeitender / Monat</p>
      <p>(Inklusive exklusiver App &amp; Zugang zur VitaStream Plattform)</p>
      <p class="label" style="margin:6px 0 2px">Erfolgsbeteiligung:</p>
      <p>Ein vereinbarter Prozentsatz der jährlichen Einsparung – gemessen an der Verbesserung des VMA Scores.</p>
    </div>
    <h2 class="h" style="margin-top:34px">Empfohlene Programmdauer</h2>
    <ul class="ticks" style="padding-left:11px"><li>3 Monate Intensivprogramm</li><li>9–12 Monate für nachhaltige Ergebnisse</li></ul>
  </div>
  <div class="box" style="top:68px;left:218px;width:190px;height:204px;padding:12px 12px">
    <h2 class="h">Digitale Begleiter: App &amp; VitaStream Portal</h2>
    <div style="padding-left:11px">
      <p>Die VMA App – Ihr interaktiver Coach im Alltag:</p>
      <ul class="ticks" style="margin-bottom:8px"><li>Persönliches Lifestyle-Tagebuch</li><li>Tipps, Übungen &amp; Rezepte</li><li>Motivierende „Vitagotchi“-Begleiter</li></ul>
      <p>Das VitaStream Portal – Wissen, das wirkt:</p>
      <ul class="ticks"><li>Exklusive Lernvideos &amp; Kurse</li><li>Rezepte, Nährstoffe &amp; Einkaufshilfen</li><li>Infotheken für Mitarbeitende &amp; Führungskräfte</li></ul>
    </div>
  </div>
  <div class="box" style="top:284px;left:218px;width:190px;height:135px;padding:12px 12px">
    <h2 class="h">Der VMA Score – Ihr Benchmark für Unternehmenserfolg</h2>
    <p style="padding-left:11px">In 72 Stunden starten – 60 Tage durchhalten – neue Gewohnheit etablieren! Denn: Veränderung beginnt mit einer Entscheidung. Nachhaltigkeit entsteht durch Wiederholung.</p>
  </div>
  <div class="box" style="top:437px;left:18px;width:390px;height:125px"></div>
  <div class="photo" style="top:408px;left:40px;width:128px;height:135px;background:linear-gradient(160deg,#5a5754,#2a2827 60%,#151414)" role="img" aria-label="Porträtfoto des Beraters im Sakko"></div>
  <div class="block" style="top:455px;left:188px;width:210px">
    <p class="cta">Jetzt anfragen &amp; Ihr Unternehmen stärken!</p>
    <p style="margin-bottom:10px">Kontaktieren Sie uns für ein unverbindliches Erstgespräch</p>
    <div class="contact-line"><svg viewBox="0 0 8 8"><rect x=".5" y="1.5" width="7" height="5" fill="#3f82b5"/><path d="M.5 1.5L4 4.5 7.5 1.5" stroke="#fff" stroke-width=".7" fill="none"/></svg>tkessler@verbindend.at</div>
    <div class="contact-line"><svg viewBox="0 0 8 8"><path d="M1.5 .5l1.5 1.5-.8 1.2a4 4 0 002.6 2.6L6 5l1.5 1.5L6.5 7.5C3.5 7.5.5 4.5.5 1.5z" fill="#3f82b5"/></svg>+43-660-5512384</div>
    <div class="contact-line"><svg viewBox="0 0 8 8" fill="none" stroke="#3f82b5" stroke-width=".8"><circle cx="4" cy="4" r="3.4"/><path d="M.6 4h6.8M4 .6c-2 2-2 4.8 0 6.8M4 .6c2 2 2 4.8 0 6.8"/></svg>www.thomas-kessler.com</div>
  </div>
  <div class="foot"><span><b style="color:var(--gold)">Unternehmensberatung</b> | Thomas Kessler, MBA</span><b>4</b></div>
</section>

<section class="page" style="left:269px;top:851px;transform:scale(.496)">
  <div class="photo" style="top:0;left:0;width:426px;height:170px;background:linear-gradient(180deg,#c9d0d4 0%,#9aa3a8 45%,#d8dcde 100%)" role="img" aria-label="Foto: Team bespricht Unterlagen an einem Tisch im Büro"></div>
  <div class="brand">Thomas Kessler</div>
  <div class="block" style="top:185px;left:38px;width:350px">
    <h2 class="h">Gesunde &amp; leistungsfähige Mitarbeitende<br>für messbare Unternehmenserfolge</h2>
    <p>Zielsetzung: Erreichen Sie eine Symbiose aus Gesundheit und Leistungsfähigkeit Ihrer Mitarbeitenden durch den innovativen "VMA Score". Dieses neuartige Benchmark-System ermöglicht eine messbare und reproduzierbare Verbesserung der Unternehmenskennzahlen durch gezielte Gesundheitsförderung.</p>
    <h2 class="h" style="margin-top:10px">Ihre Vorteile auf einen Blick:</h2>
    <ul class="dots">
      <li>Reduktion lebensstilbedingter Ermüdungserscheinungen &amp; Erschöpfungssyndrome</li>
      <li>Minimierung von Burnout &amp; Depressionen</li>
      <li>Höhere Bindung der Mitarbeitenden, geringere Fluktuation</li>
      <li>Einsparung von Wiedereinstellungs- &amp; Einschulungskosten</li>
      <li>Vermeidung von Frührente &amp; Krankenständen</li>
      <li>Stärkung Ihrer Arbeitgebermarke im "War for Talents"</li>
    </ul>
    <h2 class="h" style="margin-top:10px">Zielsetzung: Gesundheit trifft Produktivität</h2>
    <p>Ein wissenschaftlich fundiertes System zur Ermittlung gesundheitsbezogener Leistungssteigerungen. Zum Stichtag wird der Gesundheitszustand und die Leistungsfähigkeit Ihrer Mitarbeitenden anhand vorhandener Absentismus-Daten erfasst und mit Unternehmenskennzahlen und Kostenstellen verknüpft.</p>
    <h2 class="h" style="margin-top:8px">Typische Ursachen für Leistungsausfälle:</h2>
    <ul class="dots">
      <li>Fehlernährung (Makro- &amp; Mikronährstoffmangel)</li>
      <li>Mangelnde Bewegung &amp; Fitness</li>
      <li>Schlechte Schlafqualität</li>
      <li>Geringe Resilienz &amp; hoher Distress</li>
    </ul>
  </div>
  <div class="foot"><span><b style="color:var(--gold)">Unternehmensberatung</b> | Thomas Kessler, MBA</span><b>5</b></div>
</section>

<section class="page" style="left:502px;top:851px;transform:scale(.496)">
  <div class="brand">Thomas Kessler</div>
  <div class="block" style="top:70px;left:28px;width:370px">
    <h2 class="h">Zielsetzung: Gesundheit trifft Produktivität</h2>
    <div class="bignum"><span class="n">01</span><p>Impulsvortrag von Thomas Kessler: Die "Heldengeschichte" inspiriert Ihre Belegschaft, das eigene Potenzial zu entfalten. Eine Aufzeichnung steht für abwesende Mitarbeitende zur Verfügung.</p></div>
    <div class="bignum"><span class="n">02</span><p>Datenerhebung &amp; Evaluierung: Ermittlung des ersten VMA Scores und sofortiger Start erster Maßnahmen.</p></div>
    <div class="bignum"><span class="n">03</span><p>Umsetzungsphase: Begleitung durch interaktive Tools, Lerninhalte &amp; Gesundheitsangebote.</p></div>
    <h2 class="h" style="margin-top:10px">Ergebnisse auf einen Blick:</h2>
    <ul class="dots">
      <li>Wie leistungsfähig sind meine Mitarbeitenden aktuell?</li>
      <li>Welcher Wertschöpfungsverlust entsteht durch Fehlzeiten?</li>
      <li>Welchen Nutzen bringt mir die Reduktion von Leistungseinbußen?</li>
      <li>Welche (vermeidbaren) Austritts- &amp; Wiedereinstellungskosten habe ich?</li>
      <li>Wie hoch ist mein jährlicher Verlust durch krankheitsbedingte Ausfälle?</li>
    </ul>
  </div>
  <div class="block" style="top:318px;left:28px;width:185px">
    <h2 class="h">Investition in Ihre Zukunft:</h2>
    <div style="padding-left:11px">
      <p style="margin-bottom:1px">Impulsvortrag:</p>
      <p class="price">€ 25.000</p>
      <p style="margin:4px 0 1px">App-Nutzung &amp; VitaStream-Portal:</p>
      <p class="price">€ 5,90 pro Mitarbeiter:in/Monat*</p>
      <p style="margin:4px 0 0">Erfolgsbeteiligung:<br>Prozentsatz der jährlichen Einsparung gemessen an VMA Score-Verbesserung</p>
      <p style="font-style:italic;font-size:6px">*Inklusive Innovations-App mit:</p>
      <ul class="dots"><li>Interaktivem Tagebuch für Lebensstilveränderungen</li><li>Motivation durch "Vitagotchi"</li><li>Tipps, Rezepte, Übungen</li><li>Zugang zu Videos, Kursen, Infotheken u.v.m.</li></ul>
    </div>
  </div>
  <div class="box" style="top:318px;left:222px;width:186px;height:205px;padding:12px 12px">
    <h2 class="h">Dauer &amp; Nachhaltigkeit:</h2>
    <ul class="ticks" style="padding-left:11px;margin-bottom:18px"><li>Programme ab 3 Monaten (Intensiv)</li><li>Empfohlen: 9–12 Monate für nachhaltige Wirkung</li></ul>
    <h2 class="h">Die goldene VMA 72/60 Regel:</h2>
    <p style="padding-left:11px">Starten Sie innerhalb von 72 Stunden nach der Entscheidung und halten Sie 60 Tage durch – dann wird Gesundheit zur Gewohnheit!</p>
  </div>
  <div class="contact-tab">Kontakt: Lindwerk Beratung &amp; Partner KG</div>
  <div class="contact-band">
    <span class="contact-line"><svg viewBox="0 0 8 8"><path d="M1.5 .5l1.5 1.5-.8 1.2a4 4 0 002.6 2.6L6 5l1.5 1.5L6.5 7.5C3.5 7.5.5 4.5.5 1.5z" fill="#fff"/></svg>+43-660-5512384</span>
    <span class="contact-line"><svg viewBox="0 0 8 8"><rect x=".5" y="1.5" width="7" height="5" fill="#fff"/><path d="M.5 1.5L4 4.5 7.5 1.5" stroke="#3f82b5" stroke-width=".7" fill="none"/></svg>tkessler@verbindend.at</span>
    <span class="contact-line"><svg viewBox="0 0 8 8" fill="none" stroke="#fff" stroke-width=".8"><circle cx="4" cy="4" r="3.4"/><path d="M.6 4h6.8M4 .6c-2 2-2 4.8 0 6.8M4 .6c2 2 2 4.8 0 6.8"/></svg>www.thomas-kessler.com</span>
  </div>
  <div class="closing">Jetzt anfragen &amp; Mitarbeitende wie Unternehmen nachhaltig stärken!</div>
</section>

</body>
</html>
```